Business card design for a world class martial arts and group fitness facility

We need a professional and eye catching design for a business card. The card will be used in networking as well as marketing.
We are a martial arts facility offering Taekwondo, Brazilian Jiu Jitsu, and group fitness. All of our programs are geared for kids and adults.
Our Taekwondo program is lead by a Hall of Fame instructor who was Instructor of the Year in 2015.
Our Brazilian Jiu Jitsu program is lead by a wold class instructor who is also a part of the renown Brazilian KVO team.
We offer 3 focused group fitness programs: Ring striking, Driftline Conditioning, and The Meadow which are all lead by certified instructors in a small group setting.
Our facility is state of the art and has been recognized as such in nationally published magazines.
Our business is named The Lantern which is the linear logo that is attached. This is the main logo. I also attached a circular logo we have used in some marketing material. Our Jiu Jitsu program is the KVO team logo. The Taekwondo program is the TORVEX Prime. It would be nice to somehow incorporate all 3 logos, but The Lantern is most important.
Industry/Entity Type
Martial Art
Contact Information for Business Card
We would like to use all 3 logos if possible but The Lantern is the most important. We would like to have a place for a staff member's name while keeping the focus on the programs we offer.
Look and feel
Each slider illustrates characteristics of the customer's brand and the style your logo design should communicate.

```html
<!DOCTYPE html>
<html lang="en">
<head>
<meta charset="utf-8">
<title>The Lantern — Business Card</title>
<link rel="stylesheet" href="https://fonts.googleapis.com/css2?family=Lato:wght@400;700;900&display=swap">
<style>
  :root {
    --backdrop: #d6d6d4;
    --charcoal: #333333;
    --charcoal-deep: #2a2a2a;
    --brick-red: #9a0b0b;
    --logo-panel: #bdbdbd;
    --ink: #1e1e1e;
    --list-grey: #cfcfcf;
    --white: #ffffff;
    --back-light: #b4b4b4;
    --back-dark: #6a6a6a;
    --back-ink: #3a3a3a;
  }
  html, body {
    margin: 0;
    padding: 0;
    width: 1200px;
    height: 821px;
    overflow: hidden;
    background: var(--backdrop);
    font-family: "Lato", sans-serif;
  }
  .canvas {
    position: relative;
    width: 1200px;
    height: 821px;
    display: flex;
    align-items: center;
    justify-content: center;
    gap: 40px;
  }
  .card {
    position: relative;
    width: 560px;
    height: 320px;
    overflow: hidden;
    box-shadow: 0 6px 18px rgba(0,0,0,0.25);
  }

  /* Front */
  .card-front { background: var(--charcoal); }
  .front-edge {
    position: absolute; left: 0; top: 0; width: 8px; height: 100%;
    background: var(--brick-red);
  }
  .front-band {
    position: absolute; left: 263px; top: 0; width: 157px; height: 100%;
    background: var(--brick-red);
  }
  .front-right {
    position: absolute; left: 420px; top: 0; width: 140px; height: 100%;
    background: var(--charcoal-deep);
  }
  .brand-panel {
    position: absolute; left: 8px; top: 44px; width: 282px; height: 76px;
    background: var(--logo-panel);
    display: flex; align-items: center; justify-content: center;
    gap: 10px;
    box-shadow: 0 2px 6px rgba(0,0,0,0.35);
  }
  .brand-mark {
    width: 18px; height: 18px; border-radius: 50%;
    background: var(--brick-red);
  }
  .brand-name {
    font-weight: 900; font-size: 32px; color: var(--ink);
    letter-spacing: 1px; text-transform: uppercase;
  }
  .program-list {
    position: absolute; left: 30px; top: 150px; margin: 0; padding: 0;
    list-style: none;
  }
  .program-list li {
    font-weight: 700; font-size: 14px; color: var(--list-grey);
    margin-bottom: 20px;
  }
  .contact {
    position: absolute; left: 274px; top: 196px; width: 140px;
    color: var(--white); font-size: 11px; line-height: 19px;
    font-style: normal;
  }
  .partner {
    position: absolute; left: 420px; width: 140px;
    display: flex; flex-direction: column; align-items: center; gap: 5px;
  }
  .partner-kvo { top: 196px; }
  .partner-torvex { top: 262px; }
  .partner-circle {
    width: 34px; height: 34px; border-radius: 50%;
    background: #111; border: 2px solid var(--brick-red);
  }
  .partner-square {
    width: 30px; height: 30px; background: #111;
  }
  .partner-name {
    font-weight: 700; font-size: 10px; color: var(--white);
    text-transform: uppercase; letter-spacing: 0.5px;
  }

  /* Back */
  .card-back {
    background: radial-gradient(ellipse at 50% 40%, var(--back-light) 0%, var(--back-dark) 100%);
    display: flex; align-items: center; justify-content: center; gap: 16px;
  }
  .back-mark {
    width: 44px; height: 44px; border-radius: 50%;
    background: var(--back-ink);
  }
  .back-name {
    font-weight: 900; font-size: 46px; color: var(--back-ink);
    text-transform: uppercase; letter-spacing: 1px;
  }
</style>
</head>
<body>
<main class="canvas">
  <section class="card card-front" aria-label="Card front">
    <div class="front-edge"></div>
    <div class="front-band"></div>
    <div class="front-right"></div>
    <div class="brand-panel">
      <span class="brand-mark"></span>
      <span class="brand-name">The Lantern</span>
    </div>
    <ul class="program-list">
      <li>Ring striking</li>
      <li>Driftline Conditioning</li>
      <li>The Meadow</li>
    </ul>
    <address class="contact">
      575 418 209637<br>
      2150 Alder Row, Linden<br>
      hello@thelantern.com<br>
      www.thelantern.com
    </address>
    <div class="partner partner-kvo">
      <span class="partner-circle"></span>
      <span class="partner-name">KVO</span>
    </div>
    <div class="partner partner-torvex">
      <span class="partner-square"></span>
      <span class="partner-name">TORVEX Prime</span>
    </div>
  </section>

  <section class="card card-back" aria-label="Card back">
    <span class="back-mark"></span>
    <span class="back-name">The Lantern</span>
  </section>
</main>
</body>
</html>
```